Packaging artwork design for furniture

Currently our packaging is utilitarian. We want a new look that reflects our new exciting branding strategy. We want the packaging to reflect a sophisticated, expensive look. I have attached the current packaging and the logo. All the information on the box are required for the new design.
Please use between 2-3 colours, not more.

Target Market(s)

International

Industry/Entity Type

furniture

Requirements
Must have
• All the symbols but need some extra artwork
Nice to have
• artwork that portrays high end, expensive look

```html
<!DOCTYPE html>
<html lang="en">
<head>
<meta charset="UTF-8">
<title>Elmwood Living – Night Table Carton Artwork</title>
<link rel="stylesheet" href="https://fonts.googleapis.com/css2?family=Roboto+Condensed:wght@700&family=Oswald:wght@600&display=swap">
<style>
  :root {
    --kraft: #b59a7b;
    --kraft-shade: #9b8166;
    --charcoal: #464c4c;
    --charcoal-deep: #3b4040;
    --ink: #0d0d0d;
    --paper: #ffffff;
    --silver: #b9b9bb;
    --stage: #111111;
    --label: #8a7560;
  }
  * { margin: 0; padding: 0; box-sizing: border-box; }
  html, body { width: 1200px; height: 1026px; overflow: hidden; background: var(--stage); }
  .dieline { position: relative; width: 1200px; height: 1026px; }

  .panel { position: absolute; top: 150px; height: 726px; display: flex; flex-direction: column; }
  .panel--front { left: 60px; width: 560px; }
  .panel--side { left: 640px; width: 500px; }

  .band-top { position: relative; height: 212px; background: var(--kraft); }
  .panel--side .band-top { background: var(--kraft-shade); }
  .band-main { position: relative; height: 385px; background: var(--charcoal); }
  .panel--side .band-main { background: var(--charcoal-deep); }
  .stripe-light { height: 38px; background: var(--paper); }
  .panel--side .stripe-light { background: var(--silver); }
  .stripe-dark { height: 53px; background: var(--ink); }
  .band-base { flex: 1; background: var(--kraft); }
  .panel--side .band-base { background: var(--kraft-shade); }

  .orientation-mark { position: absolute; left: 70px; top: 44px; display: flex; align-items: flex-end; gap: 8px; color: var(--ink); }
  .orientation-mark .word { font-family: "Oswald", sans-serif; font-weight: 600; font-size: 50px; line-height: 1; }
  .address-window { position: absolute; left: 330px; top: 64px; width: 186px; height: 128px; border: 2.5px dotted #2a2520; }

  .brand-name {
    font-family: "Roboto Condensed", sans-serif;
    font-weight: 700;
    text-transform: uppercase;
    color: var(--paper);
    white-space: nowrap;
    text-align: center;
    position: absolute; left: 0; right: 0;
  }
  .panel--front .brand-name { top: 188px; font-size: 36px; letter-spacing: 3px; }
  .panel--side .brand-name { top: 92px; font-size: 22px; letter-spacing: 2px; color: #d8d8d8; }

  .handling-icons { position: absolute; right: 36px; top: 70px; display: flex; gap: 14px; }
  .handling-icons svg { width: 56px; height: 60px; }

  .product-label { position: absolute; left: 96px; top: 165px; width: 330px; height: 180px; background: var(--label); padding: 34px 26px; font-family: "Roboto Condensed", sans-serif; font-weight: 700; font-size: 22px; line-height: 31px; color: var(--ink); }
</style>
</head>
<body>
<main class="dieline">
  <section class="panel panel--front">
    <div class="band-top">
      <div class="orientation-mark">
        <svg width="18" height="58" viewBox="0 0 18 58"><path d="M9 2 L17 16 H11 V56 H7 V16 H1 Z" fill="currentColor"/></svg>
        <span class="word">UP</span>
        <svg width="18" height="58" viewBox="0 0 18 58"><path d="M9 2 L17 16 H11 V56 H7 V16 H1 Z" fill="currentColor"/></svg>
      </div>
      <div class="address-window"></div>
    </div>
    <div class="band-main">
      <p class="brand-name">Elmwood Living</p>
    </div>
    <div class="stripe-light"></div>
    <div class="stripe-dark"></div>
    <div class="band-base"></div>
  </section>

  <section class="panel panel--side">
    <div class="band-top">
      <div class="handling-icons">
        <svg viewBox="0 0 56 60" aria-label="This way up"><rect x="2" y="2" width="52" height="56" rx="3" fill="none" stroke="#111" stroke-width="2.5"/><path d="M20 14 L26 22 H22 V42 H18 V22 H14 Z M36 14 L42 22 H38 V42 H34 V22 H30 Z" fill="#111"/><rect x="13" y="45" width="30" height="3" fill="#111"/></svg>
        <svg viewBox="0 0 56 60" aria-label="Fragile"><rect x="2" y="2" width="52" height="56" rx="3" fill="none" stroke="#111" stroke-width="2.5"/><path d="M18 12 H38 L36 28 Q28 36 20 28 Z" fill="#111"/><rect x="26.5" y="32" width="3" height="14" fill="#111"/><rect x="19" y="45" width="18" height="3" fill="#111"/></svg>
        <svg viewBox="0 0 56 60" aria-label="Keep dry"><rect x="2" y="2" width="52" height="56" rx="3" fill="none" stroke="#111" stroke-width="2.5"/><path d="M10 30 Q28 8 46 30 Z" fill="#111"/><path d="M28 30 V44 Q28 48 24 48 Q21 48 21 45" fill="none" stroke="#111" stroke-width="2.5"/></svg>
        <svg viewBox="0 0 56 60" aria-label="Handle with care"><rect x="2" y="2" width="52" height="56" rx="3" fill="none" stroke="#111" stroke-width="2.5"/><rect x="20" y="18" width="16" height="14" fill="#111"/><path d="M10 24 L20 36 H36 L46 24 L46 36 L38 46 H18 L10 36 Z" fill="none" stroke="#111" stroke-width="2.5"/></svg>
        <svg viewBox="0 0 56 60" aria-label="Flammable"><rect x="2" y="2" width="52" height="56" rx="3" fill="none" stroke="#111" stroke-width="2.5"/><path d="M28 10 Q40 24 38 36 Q36 48 28 48 Q18 48 17 38 Q16 28 24 20 Q24 30 29 32 Q26 22 28 10 Z" fill="#111"/></svg>
      </div>
    </div>
    <div class="band-main">
      <p class="brand-name">Elmwood Living</p>
      <div class="product-label">
        <p>MODEL : KT480-NS07</p>
        <p>ITEM : NIGHT TABLE</p>
        <p>QUANTITY : 1/1</p>
        <p>CBM :</p>
      </div>
    </div>
    <div class="stripe-light"></div>
    <div class="stripe-dark"></div>
    <div class="band-base"></div>
  </section>
</main>
</body>
</html>
```